Executive Performance Review mapped on J-curve

I need to turn an executive company performance review into a visual infographic. The list of accomplishments is grouped into four calendar quarters. Each quarter needs a subtle representation of the season. The four quarters and associated list of accomplishments need to be mapped to a J-curve. - Spreadsheet with accomplishments attached (Throughput)- Sample image of a J-curve. You can google J-curve to see more images.- The title should be "Danela Morsky Year in Review"

Target Market(s)

Board of Directors

Requirements
Nice to have
• This will be presented to a company founder that is an artist and customer experience expert. He is very visual so a nice visual representation of the data will be impactful. He also uses the phrase that you have to live with or work with someone for four seasons before you really know them. This is why I have the seasons mapped to the quarters. The Fall season motif should be gloomy and stormy.

```html
<!DOCTYPE html>
<html lang="en">
<head>
<meta charset="utf-8">
<title>Danela Morsky Year in Review</title>
<link href="https://fonts.googleapis.com/css2?family=Montserrat:wght@400;500&family=Oswald:wght@500&family=Play:wght@400;700&display=swap" rel="stylesheet">
<style>
:root{
  --navy:#0f1d4d;
  --orange:#f05a28;
  --teal:#1bb9a3;
  --white:#ffffff;
  --grid:#2d3a66;
  --axis:#3a4770;
  --curve:#0aa04a;
  --dot:#e8413c;
  --tick:#3c4a78;
}
*{margin:0;padding:0;box-sizing:border-box}
html,body{width:1200px;height:3437px;overflow:hidden;background:var(--navy)}
body{position:relative;font-family:"Montserrat",sans-serif;color:var(--white)}
.title{position:absolute;top:78px;left:0;width:1200px;text-align:center;color:var(--orange);font-family:"Montserrat",sans-serif;font-weight:400;font-size:76px;line-height:90px;letter-spacing:-1px}
.chart{position:absolute;left:0;top:230px}
.season{position:absolute}
.season-name{font-family:"Oswald",sans-serif;font-weight:500;color:var(--teal);font-size:42px;line-height:42px;letter-spacing:-0.5px}
.season-quarter{font-family:"Oswald",sans-serif;font-weight:500;color:var(--teal);font-size:30px;line-height:34px}
.block{position:absolute}
.block h3{font-family:"Play",sans-serif;font-weight:700;color:var(--orange);font-size:24px;line-height:30px;letter-spacing:1px}
.block p{font-size:16px;line-height:25px;color:var(--white)}
.block p.gap{margin-top:10px}
.block + .block{}
.stack h3{margin-top:14px}
.stack h3:first-child{margin-top:0}
.divider{position:absolute;left:43px;width:1102px;height:0;border-top:5px dotted var(--orange)}
.tree{position:absolute;border-radius:48% 52% 20% 20%}
.tree-summer{left:40px;top:1021px;width:387px;height:454px;background:radial-gradient(ellipse at 50% 35%,#e9a6c9 0%,#8cbf4c 40%,#7a4a22 80%,transparent 82%)}
.tree-fall{left:701px;top:1669px;width:380px;height:434px;background:radial-gradient(ellipse at 50% 35%,#9ccc4e 0%,#78b33a 45%,#7a4a22 78%,transparent 80%)}
.tree-winter{left:47px;top:2270px;width:347px;height:427px;background:radial-gradient(ellipse at 50% 50%,#f2c23a 0%,#e2552a 30%,#6b4524 70%,transparent 72%)}
.tree-spring{left:721px;top:2830px;width:360px;height:454px;background:radial-gradient(ellipse at 50% 50%,#5b6a7a 0%,#3d4a62 45%,#1d2a55 72%,transparent 74%)}
</style>
</head>
<body>

<h1 class="title">Danela Morsky Year<br>in Review</h1>

<svg class="chart" width="1200" height="680" viewBox="0 230 1200 680" aria-label="J-curve of the year by season">
  <g stroke="var(--grid)" stroke-width="1.5">
    <line x1="186" y1="243" x2="186" y2="850"/><line x1="273" y1="243" x2="273" y2="850"/>
    <line x1="360" y1="243" x2="360" y2="850"/><line x1="446" y1="243" x2="446" y2="850"/>
    <line x1="533" y1="243" x2="533" y2="850"/><line x1="619" y1="243" x2="619" y2="850"/>
    <line x1="706" y1="243" x2="706" y2="850"/><line x1="792" y1="243" x2="792" y2="850"/>
    <line x1="879" y1="243" x2="879" y2="850"/><line x1="965" y1="243" x2="965" y2="850"/>
    <line x1="1052" y1="243" x2="1052" y2="850"/>
    <line x1="100" y1="763" x2="1135" y2="763"/><line x1="100" y1="676" x2="1135" y2="676"/>
    <line x1="100" y1="589" x2="1135" y2="589"/><line x1="100" y1="502" x2="1135" y2="502"/>
    <line x1="100" y1="415" x2="1135" y2="415"/><line x1="100" y1="328" x2="1135" y2="328"/>
  </g>
  <g stroke="var(--axis)" stroke-width="6">
    <line x1="100" y1="243" x2="100" y2="850"/>
    <line x1="100" y1="850" x2="1135" y2="850"/>
  </g>
  <g fill="var(--tick)" font-family="Montserrat, sans-serif" font-size="21" text-anchor="middle">
    <text x="71" y="884">0</text><text x="186" y="884">1</text><text x="273" y="884">2</text>
    <text x="360" y="884">3</text><text x="446" y="884">4</text><text x="533" y="884">5</text>
    <text x="619" y="884">6</text><text x="706" y="884">7</text><text x="792" y="884">8</text>
    <text x="879" y="884">9</text><text x="965" y="884">10</text><text x="1052" y="884">11</text>
    <text x="71" y="770">1</text><text x="71" y="683">2</text><text x="71" y="596">3</text>
    <text x="71" y="509">4</text><text x="71" y="422">5</text><text x="71" y="335">6</text>
  </g>
  <path d="M103 654 C200 730 320 790 422 789 C540 788 640 750 733 710 C850 650 960 540 1015 428 L1039 375" fill="none" stroke="var(--curve)" stroke-width="6"/>
  <circle cx="99" cy="850" r="12" fill="var(--dot)"/>
  <g fill="var(--white)" stroke="var(--dot)" stroke-width="8">
    <circle cx="103" cy="654" r="16"/><circle cx="422" cy="789" r="16"/>
    <circle cx="733" cy="710" r="16"/><circle cx="1015" cy="428" r="16"/>
  </g>
  <g fill="var(--orange)" font-family="Play, sans-serif" font-weight="700" font-size="25">
    <text x="59" y="616">Summer</text>
    <text x="403" y="747">Fall</text>
    <text x="687" y="661">Winter</text>
    <text x="1010" y="495">Spring</text>
  </g>
</svg>

<!-- Summer -->
<div class="tree tree-summer" role="img" aria-label="Illustration of a tree in summer bloom with pink blossoms and green leaves"></div>
<div class="season" style="left:514px;top:972px">
  <div class="season-name">SUMMER</div>
  <div class="season-quarter">Q3 2018</div>
</div>
<div class="block stack" style="left:514px;top:1084px;width:280px">
  <h3>Transitions</h3>
  <p>RO Transition from Reid &amp; Lina<br>Start CR Office Initiative<br>Tactical Ops transition from Reid<br>Formalize Exec Team</p>
  <h3 style="margin-top:22px">Biz Architecture</h3>
  <p>Independent Financial Audit<br>Organizational Audit - Structure<br>Organizational Audit - People<br>XF Framework - ESU</p>
  <p class="gap" style="margin-top:22px">Defined Utilization, Realization,<br>Availability</p>
</div>
<div class="block stack" style="left:814px;top:1084px;width:290px">
  <h3>Strategy</h3>
  <p>Effective Strategy Meeting</p>
  <p style="margin-top:8px;line-height:21px">Strategic Themes 2018 - 2020:<br>Stablize, Accelerate, Surge</p>
  <p style="margin-top:10px;line-height:21px">Business Drivers: Drive Revenue,<br>Improve Velora Experience,<br>Increase Brand Awareness</p>
  <h3 style="margin-top:6px">Sales</h3>
  <p>Halvers Account Transition</p>
  <p style="margin-top:10px">NVQ Account Transition</p>
  <p style="margin-top:10px;line-height:21px">2 year Managed Services<br>Engagement Model</p>
  <h3 style="margin-top:14px">Revenue / EBITA</h3>
  <p style="line-height:18px">TBD</p>
</div>

<div class="divider" style="top:1577px"></div>

<!-- Fall -->
<div class="season" style="left:48px;top:1645px">
  <div class="season-name">FALL</div>
  <div class="season-quarter">Q4 2018</div>
</div>
<div class="block stack" style="left:48px;top:1740px;width:290px">
  <h3>Biz Architecture</h3>
  <p>XF Framework - Functional<br>Meetings &amp; Scrum of Scrums<br>Structured Reorg<br>Implemented Reorg<br>Quarterly Org Iteration cadence<br>Defined Key Hire Plan<br>CR Office Operational<br>Time Accountability<br>Tools ReConfig<br>Org Structure v1</p>
</div>
<div class="block stack" style="left:364px;top:1740px;width:300px">
  <h3>Strategy</h3>
  <p style="line-height:20px">Internal QBR Accountability</p>
  <h3 style="margin-top:10px">Sales</h3>
  <p>Tarrow QBR<br>Halvers QBR</p>
  <h3 style="margin-top:12px">Revenue / EBITA</h3>
  <p>TBD</p>
</div>
<div class="tree tree-fall" role="img" aria-label="Illustration of a full green leafy tree"></div>

<div class="divider" style="top:2174px"></div>

<!-- Winter -->
<div class="tree tree-winter" role="img" aria-label="Illustration of a bare tree dropping yellow and red autumn leaves into a pile"></div>
<div class="season" style="left:514px;top:2268px">
  <div class="season-name">WINTER</div>
  <div class="season-quarter">Q1 2019</div>
</div>
<div class="block stack" style="left:514px;top:2370px;width:290px">
  <h3>Biz Architecture</h3>
  <p>XF Framework - Progress<br>Demos &nbsp;Org Structure - COE's<br>Stablize Accounting &amp; Finance<br>Exec Hiring Process</p>
  <h3 style="margin-top:8px">Key Hires</h3>
  <p>Controller<br>Director CX</p>
</div>
<div class="block stack" style="left:817px;top:2370px;width:300px">
  <h3>Strategy</h3>
  <p>Founders removed from front<br>line activity Vantis QBR - Goal<br>Setting &amp; Tracking</p>
  <h3 style="margin-top:10px">Sales</h3>
  <p>NVQ QBR<br>Halvers QBR</p>
  <h3 style="margin-top:12px">Revenue / EBITA</h3>
  <p style="line-height:18px">TBD</p>
</div>

<div class="divider" style="top:2779px"></div>

<!-- Spring -->
<div class="season" style="left:44px;top:2852px">
  <div class="season-name">SPRING</div>
  <div class="season-quarter">Q2 2019</div>
</div>
<div class="block stack" style="left:44px;top:2946px;width:300px">
  <h3>Biz Architecture</h3>
  <p style="line-height:18px;margin-top:4px">Tiered Pricing Pre-Paid<br>Engagement Model</p>
  <p style="margin-top:4px">XF Framework - Ideation Board<br>Consulting Levels &amp; Salary Bands<br>Roles &amp; Responsibilities</p>
  <h3 style="margin-top:30px">Key Hires</h3>
  <p>Interim HR<br>Provisional Client Partner<br>Acting Director 1<br>Acting Director 2<br>Client Partner 1<br>Sales Exec 1</p>
</div>
<div class="block stack" style="left:367px;top:2946px;width:320px">
  <h3>Sales</h3>
  <p>Opened BrightPane Door</p>
  <p style="line-height:16px;margin-top:4px">Flipped focus from<br>operationaly run company</p>
  <p style="margin-top:4px">to sales/marketing driven org<br>QRN Direct</p>
  <h3 style="margin-top:30px">Revenue / EBITA</h3>
  <p>TBD</p>
</div>
<div class="tree tree-spring" role="img" aria-label="Illustration of a bare leafless winter tree in cool grey tones"></div>

</body>
</html>
```